braided hoses

Tue, Jun 25, 3:27 PM (17 hours ago)

WE ARE LOOKING FOR A FLYER WE CAN EMAIL OU TO EXISTING CUSTOMERS - MECHANICAL INDUSTRIAL WHOLESALE ETC

WE SUPPLY PERFORMANCE FITTINGS TO MAKE BRAIDED HOSE FOR RACECAR, ENTHUSIASTS AND GENERAL CARS
these are used for
brake hoses
cooler lines
oil + fuel hoses

pictures supplied but if better pictures found will be ok
i do not want to pay for pictures afterwards

Requirements
Must have
• company details correct

```html
<!DOCTYPE html>
<html lang="en">
<head>
<meta charset="utf-8">
<title>Ridgeline Auto Centre – Braided Hose Fittings Flyer</title>
<link rel="stylesheet" href="https://fonts.googleapis.com/css2?family=Bebas+Neue&family=Poppins:ital,wght@0,400;0,500;0,600;0,700;1,500&display=swap">
<style>
  :root {
    --yellow: #fdd700;
    --ink: #111114;
    --panel: #3d3d42;
    --band: #e4e4e7;
    --white: #ffffff;
    --soft-white: #ececec;
    --footer-text: #333338;
  }
  html, body {
    margin: 0;
    width: 1200px;
    height: 1200px;
    overflow: hidden;
    background: var(--white);
  }
  .flyer {
    position: absolute;
    left: 134px;
    top: 0;
    width: 931px;
    height: 1200px;
    background: var(--band);
    overflow: hidden;
    font-family: "Poppins", sans-serif;
  }
  .top-band {
    position: absolute;
    left: 0; top: 0;
    width: 100%; height: 116px;
    background: var(--band);
  }
  .top-band__rule {
    position: absolute;
    left: 0; top: 61px;
    width: 39px; height: 3px;
    background: var(--yellow);
  }
  .top-band__url {
    position: absolute;
    left: 55px; top: 45px;
    font-size: 23px;
    font-weight: 500;
    letter-spacing: 1.6px;
    color: var(--ink);
    line-height: 1;
  }
  .hero-photo {
    position: absolute;
    left: 0; top: 116px;
    width: 100%; height: 459px;
    background:
      radial-gradient(ellipse at 72% 50%, rgba(200,190,185,0.75) 0%, rgba(200,190,185,0) 45%),
      linear-gradient(90deg, #b9c2cf 0%, #e6e8ec 25%, #f1f1f3 45%, #d9dce2 70%, #3c4a6a 92%, #2e3a58 100%);
  }
  .brand-box {
    position: absolute;
    left: 611px; top: 23px;
    width: 254px; height: 184px;
    background: var(--yellow);
    display: flex;
    align-items: center;
    justify-content: center;
    text-align: center;
  }
  .brand-box__name {
    font-family: "Poppins", sans-serif;
    font-weight: 700;
    font-size: 22px;
    line-height: 1.2;
    color: var(--ink);
    letter-spacing: 0.5px;
  }
  .headline {
    position: absolute;
    left: 54px; top: 222px;
    margin: 0;
    font-family: "Bebas Neue", sans-serif;
    font-weight: 400;
    font-size: 100px;
    line-height: 81px;
    letter-spacing: 1.5px;
    color: var(--ink);
  }
  .info-panel {
    position: absolute;
    left: 0; top: 575px;
    width: 100%; height: 497px;
    background: var(--panel);
  }
  .product-frame {
    position: absolute;
    left: 42px;
    width: 321px; height: 262px;
    background: #f4f4f4;
  }
  .product-frame--fitting { top: 492px; }
  .product-frame--hose { top: 773px; }
  .product-frame__shot {
    position: absolute;
    left: 12px; top: 12px;
    width: 299px; height: 240px;
  }
  .product-frame--fitting .product-frame__shot {
    background: radial-gradient(ellipse at 40% 45%, #c23a44 0%, #2f55c8 30%, var(--yellow) 58%);
  }
  .product-frame--hose .product-frame__shot {
    background: linear-gradient(160deg, var(--yellow) 20%, #8a8780 45%, var(--yellow) 55%, #8a8780 75%, var(--yellow) 90%);
  }
  .pitch {
    position: absolute;
    left: 411px; top: 601px;
    width: 480px;
    margin: 0;
    font-size: 28.5px;
    font-weight: 600;
    line-height: 40.6px;
    color: var(--white);
    letter-spacing: 0.2px;
  }
  .pitch__highlight { color: var(--yellow); }
  .uses-bar {
    position: absolute;
    left: 408px; top: 826px;
    width: 466px; height: 50px;
    background: var(--yellow);
  }
  .uses-bar__title {
    position: absolute;
    left: 19px; top: 0;
    margin: 0;
    line-height: 50px;
    font-size: 25px;
    font-weight: 700;
    color: var(--ink);
  }
  .uses-list {
    position: absolute;
    left: 420px; top: 886px;
    margin: 0; padding: 0;
    list-style: none;
  }
  .uses-list__item {
    display: flex;
    align-items: center;
    height: 41px;
    font-size: 30px;
    font-weight: 400;
    color: var(--soft-white);
    letter-spacing: 0.8px;
  }
  .uses-list__tick {
    width: 30px; height: 26px;
    margin-right: 16px;
  }
  .footer {
    position: absolute;
    left: 0; top: 1072px;
    width: 100%; height: 128px;
    background: var(--band);
  }
  .footer__contact {
    position: absolute;
    left: 54px;
    display: flex;
    align-items: center;
    color: var(--footer-text);
    font-size: 21px;
    line-height: 1;
  }
  .footer__contact--address { top: 36px; font-weight: 600; }
  .footer__contact--email { top: 66px; font-weight: 500; }
  .footer__icon {
    width: 20px; height: 20px;
    margin-right: 10px;
  }
  .call-badge {
    position: absolute;
    left: 550px; top: 25px;
    width: 74px; height: 74px;
    border-radius: 50%;
    background: var(--yellow);
    display: flex;
    align-items: center;
    justify-content: center;
  }
  .call-badge__icon { width: 38px; height: 38px; }
  .call-text {
    position: absolute;
    left: 642px; top: 34px;
    color: var(--ink);
  }
  .call-text__prompt {
    display: block;
    font-size: 20px;
    font-style: italic;
    font-weight: 500;
    line-height: 1;
  }
  .call-text__number {
    display: block;
    margin-top: 4px;
    font-size: 36px;
    font-weight: 700;
    line-height: 1;
    letter-spacing: 0.5px;
  }
</style>
</head>
<body>
<main class="flyer">
  <header class="top-band">
    <span class="top-band__rule"></span>
    <span class="top-band__url">www.ridgelineautocentre.co.nz</span>
  </header>

  <div class="hero-photo" role="img" aria-label="Mechanic's hands tightening a metal fitting with a wrench in a workshop"></div>

  <div class="brand-box">
    <span class="brand-box__name">RIDGELINE<br>AUTO CENTRE</span>
  </div>

  <h1 class="headline">Mechanical<br>Industrial<br>Wholesale etc</h1>

  <section class="info-panel"></section>

  <figure class="product-frame product-frame--fitting" style="margin:0">
    <div class="product-frame__shot" role="img" aria-label="Red and blue anodised 90 degree braided hose fitting"></div>
  </figure>
  <figure class="product-frame product-frame--hose" style="margin:0">
    <div class="product-frame__shot" role="img" aria-label="Lengths of stainless steel braided hose"></div>
  </figure>

  <p class="pitch">WE SUPPLY <span class="pitch__highlight">PERFORMANCE FITTINGS TO MAKE BRAIDED HOSE FOR RACECAR</span>, ENTHUSIASTS AND GENERAL CARS</p>

  <div class="uses-bar">
    <h2 class="uses-bar__title">These are used for :</h2>
  </div>

  <ul class="uses-list">
    <li class="uses-list__item">
      <svg class="uses-list__tick" viewBox="0 0 30 26"><path d="M3 13 L11 21 L27 4" fill="none" stroke="#fdd700" stroke-width="4.5" stroke-linecap="round" stroke-linejoin="round"/></svg>
      Brake hoses
    </li>
    <li class="uses-list__item">
      <svg class="uses-list__tick" viewBox="0 0 30 26"><path d="M3 13 L11 21 L27 4" fill="none" stroke="#fdd700" stroke-width="4.5" stroke-linecap="round" stroke-linejoin="round"/></svg>
      Cooler lines
    </li>
    <li class="uses-list__item">
      <svg class="uses-list__tick" viewBox="0 0 30 26"><path d="M3 13 L11 21 L27 4" fill="none" stroke="#fdd700" stroke-width="4.5" stroke-linecap="round" stroke-linejoin="round"/></svg>
      Oil + fuel hoses
    </li>
  </ul>

  <footer class="footer">
    <div class="footer__contact footer__contact--address">
      <svg class="footer__icon" viewBox="0 0 20 20"><path d="M10 1a6 6 0 0 0-6 6c0 4.5 6 12 6 12s6-7.5 6-12a6 6 0 0 0-6-6zm0 8.3a2.3 2.3 0 1 1 0-4.6 2.3 2.3 0 0 1 0 4.6z" fill="#333338"/></svg>
      48 Kestrel Rd, Marlow, Hamilton
    </div>
    <div class="footer__contact footer__contact--email">
      <svg class="footer__icon" viewBox="0 0 20 20"><rect x="2" y="5" width="16" height="11" rx="1.5" fill="none" stroke="#333338" stroke-width="1.6"/><path d="M2.5 6 L10 11.5 L17.5 6" fill="none" stroke="#333338" stroke-width="1.6"/></svg>
      parts@ridgelineautocentre.co.nz
    </div>

    <div class="call-badge">
      <svg class="call-badge__icon" viewBox="0 0 40 40">
        <path d="M9 4c1.5-1 3-.8 4 .6l3.6 5.4c.9 1.3.6 2.8-.6 3.8l-2.4 1.9c1.6 4 4.6 7 8.6 8.6l1.9-2.4c1-1.2 2.5-1.5 3.8-.6l5.4 3.6c1.4 1 1.6 2.5.6 4l-2 2.8c-1.3 1.8-3.6 2.5-5.6 1.7C16.8 30.5 9.5 23.2 6.6 13.7 6 11.7 6.6 9.4 8.4 8.1z" fill="#111114"/>
        <path d="M23 10a8 8 0 0 1 7 7" fill="none" stroke="#111114" stroke-width="2.4" stroke-linecap="round"/>
        <path d="M23 4a14 14 0 0 1 13 13" fill="none" stroke="#111114" stroke-width="2.4" stroke-linecap="round"/>
      </svg>
    </div>
    <div class="call-text">
      <span class="call-text__prompt">Call to find out more</span>
      <span class="call-text__number">0800 555 318</span>
    </div>
  </footer>
</main>
</body>
</html>
```